Tavo Payments Business card refresh

Need a new design of our business card The info is not what is on these cards i sent this for a reference. I can email all the info over
Info would be Derek Whitfield Chief TAVO is the title. our new address is 47615 Birch Hollow Rd. Alder Springs Or 91384 Cell number is 555-634-2917 Work number is 855-482-7309 ext 212 Derek@tavopayments.com is my email address
Target Market(s)
Merchant Services all businesses that take credit cards
Industry/Entity Type
Merchant Services / Credit Card processing
Contact Information for Business Card
Need a new design of our business card The info is not what is on these cards i sent this for a reference. I can email all the info over Info would be Derek Whitfield Chief TAVO is the title. our new address is 47615 Birch Hollow Rd. Alder Springs Or 91384 Cell number is 555-634-2917 Work number is 855-482-7309 ext 212 Derek@tavopayments.com is my email address
Requirements
Must have
- My logo and colors from my brand guidelines
Nice to have
- i sent some designs just need a new refresh
Should not have
- nothing specific

```html
<!DOCTYPE html>
<html lang="en">
<head>
<meta charset="utf-8">
<title>Tavo Payments Business Card</title>
<link href="https://fonts.googleapis.com/css2?family=Lato:wght@300;400;700;900&display=swap" rel="stylesheet">
<style>
  :root {
    --backdrop: #1f2023;
    --card: #1e1f22;
    --ink: #ffffff;
    --brand-green: #93c01f;
  }
  * { margin: 0; padding: 0; box-sizing: border-box; }
  html, body {
    width: 1200px; height: 1200px; overflow: hidden;
    background: var(--backdrop);
    font-family: "Lato", sans-serif;
  }
  .card {
    position: absolute;
    left: 229px; width: 742px; height: 423px;
    background: var(--card);
    box-shadow: 0 12px 28px rgba(0,0,0,0.45);
  }
  .card--front { top: 137px; }
  .card--back { top: 642px; }

  .brand {
    position: absolute;
    display: flex; align-items: center; gap: 12px;
    color: var(--ink);
    font-weight: 900;
    letter-spacing: 0.5px;
    white-space: nowrap;
    line-height: 1;
  }
  .brand__mark { background: var(--brand-green); flex: none; }
  .card--front .brand { left: 59px; top: 76px; font-size: 34px; }
  .card--front .brand__mark { width: 22px; height: 22px; }
  .card--back .brand {
    left: 50%; top: 51%; transform: translate(-50%, -50%);
    font-size: 46px;
  }
  .card--back .brand__mark { width: 30px; height: 30px; }

  .holder { position: absolute; left: 60px; top: 228px; }
  .holder__name {
    color: var(--brand-green);
    font-weight: 700; font-size: 31px; line-height: 1;
  }
  .holder__title {
    color: var(--ink);
    font-weight: 400; font-size: 18px; line-height: 1; margin-top: 7px;
  }

  .contact {
    position: absolute; left: 62px; top: 314px;
    list-style: none;
    color: var(--ink);
    font-weight: 300; font-size: 18px;
  }
  .contact li { display: flex; align-items: center; height: 24.7px; white-space: nowrap; }
  .contact svg { width: 15px; height: 15px; margin-right: 8px; fill: var(--brand-green); }

  .location {
    position: absolute; right: 56px; top: 314px;
    text-align: right;
    font-style: normal;
    color: var(--ink);
    font-weight: 300; font-size: 18px; line-height: 24.7px;
    white-space: nowrap;
  }
  .location__web { color: var(--brand-green); }
</style>
</head>
<body>
  <section class="card card--front">
    <div class="brand"><span class="brand__mark"></span>Tavo Payments</div>

    <div class="holder">
      <div class="holder__name">DEREK WHITFIELD</div>
      <div class="holder__title">Chief TAVO</div>
    </div>

    <ul class="contact">
      <li>
        <svg viewBox="0 0 16 16" aria-hidden="true"><path d="M4 0h8a1.5 1.5 0 0 1 1.5 1.5v13A1.5 1.5 0 0 1 12 16H4a1.5 1.5 0 0 1-1.5-1.5v-13A1.5 1.5 0 0 1 4 0zm.5 2v10.5h7V2zm3.5 11.3a.9.9 0 1 0 0 1.8.9.9 0 0 0 0-1.8z"/></svg>
        555-634-2917
      </li>
      <li>
        <svg viewBox="0 0 16 16" aria-hidden="true"><path d="M3.6 1.2l2 2.6c.3.4.3 1-.1 1.4L4.4 6.3c.9 2.2 2.9 4.3 5.3 5.3l1.1-1.1c.4-.4 1-.4 1.4-.1l2.6 2c.4.3.5.9.1 1.3l-1.3 1.4C12.2 16.6 0 9.8 1.6 2.4L2.3 1.2c.4-.5 1-.5 1.3 0zM9.5 1a5.5 5.5 0 0 1 5.5 5.5h-1.4A4.1 4.1 0 0 0 9.5 2.4zm0 2.6a2.9 2.9 0 0 1 2.9 2.9H11a1.5 1.5 0 0 0-1.5-1.5z"/></svg>
        855-482-7309
      </li>
      <li>
        <svg viewBox="0 0 16 16" aria-hidden="true"><path d="M0 3h16v1.6L8 9 0 4.6zm0 3.3l8 4.4 8-4.4V13H0z"/></svg>
        Derek@tavopayments.com
      </li>
    </ul>

    <address class="location">
      47615 Birch Hollow<br>
      Rd. Alder Springs Or 91384<br>
      <span class="location__web">www.tavopayments.com</span>
    </address>
  </section>

  <section class="card card--back">
    <div class="brand"><span class="brand__mark"></span>Tavo Payments</div>
  </section>
</body>
</html>
```